Sip. Stroll. Flourish. Book Cover

I would like a book cover for the print edition book I am self publishing. My cover will require front, back, and spine design. I have provided a template to assist with sizing and spacing.

My book is named "Sip. Stroll. Flourish. A Simple Diet, Drive to Stretch, and Outlook Manual Building Traction Along Better Vigor and Balance" by Gregory Talbrecht RD, CPT. I use the concept of waves as an analogy for forward progress in life and would like that reflected in the cover design. I would like the color scheme to be blacks, whites, grey, and various shades of blue. I have provided a style guide for reference. Please include my logo on the front, spine, and back of the design. Please include an about the author, book summary, and my picture on the back. I have provided the wording below.

About the Author: Gregory Talbrecht is a Registered Dietitian and Certified Personal Trainer from Cleveland, OH. He graduated from the Verdant Plains University and currently works as a health coach in the healthcare industry. His passions are fitness, nutrition, science, and motivation. He has extensive knowledge and experience in wellness, healthcare, and disease treatment and disease. Gregory has worked with hundreds of people through counseling, consulting, and coaching in an effort to make a difference in their long-term health. In his spare time, he enjoys exercising, watching movies, and trying out new foods.

Book Summary: Believe in you. Trust in You. Sip. Stroll. Flourish. is a book committed to you. Behavior change and improved health can be challenging. You must feel empowered to make decisions and changes create momentum in the right direction. But, you may not always have the knowledge to do that. This book provides you with practical and fun tools and tips to improve your nutrition, motivation to move, and mindset. You are awesome. You are beautiful. You have the power to control your destiny and future. All you have to do is Sip, Stroll, and Flourish!

Please use a modern/ futuristic font style for the title. I have also provided some draft book covers for inspiration/ direction. Thank you!

Colors

Designer to choose only greyscale colors for use in the design.

Requirements
Must have
• Color scheme, about author, profile picture, and book summary on back, wave themed graphics

```html
<!DOCTYPE html>
<html lang="en">
<head>
<meta charset="utf-8">
<title>Sip. Stroll. Flourish. – Book Cover</title>
<link href="https://fonts.googleapis.com/css2?family=Dosis:wght@400;500;600;700&display=swap" rel="stylesheet">
<style>
  :root{
    --backdrop:#e9e9ea;
    --floor:#ffffff;
    --cover-dark:#1a2531;
    --cover-mid:#2b3a49;
    --spine:#485a6a;
    --spine-ink:#0f1821;
    --ink-light:#f2f5f8;
    --rule:#d8f1f8;
    --brand-blue:#7fb2dc;
    --wave:#8fc3e6;
  }
  *{box-sizing:border-box;margin:0;padding:0}
  html,body{width:1200px;height:946px;overflow:hidden}
  body{background:var(--backdrop);font-family:'Dosis',sans-serif;color:var(--ink-light);position:relative}
  .floor{position:absolute;left:0;top:936px;width:1200px;height:10px;background:var(--floor)}
  .cover{position:absolute;left:94px;top:94px;width:1012px;height:756px;box-shadow:8px 8px 10px rgba(0,0,0,.35)}
  .back{position:absolute;left:0;top:0;width:474px;height:756px;overflow:hidden;
        background:linear-gradient(160deg,var(--cover-mid) 0%,var(--cover-dark) 55%,#141d27 100%)}
  .spine{position:absolute;left:474px;top:0;width:64px;height:756px;background:var(--spine);
         border-left:1px solid #5d6f80;border-right:1px solid #5d6f80}
  .front{position:absolute;left:538px;top:0;width:474px;height:756px;overflow:hidden;
         background:linear-gradient(180deg,var(--cover-mid) 0%,var(--cover-dark) 100%)}

  .waves{position:absolute;left:0;width:474px;pointer-events:none}
  .waves path{fill:none;stroke:var(--wave)}
  .back .waves{top:0;height:756px}
  .front .waves{top:0;height:180px}

  .author-photo{position:absolute;left:32px;top:92px;width:144px;height:231px;
        background:linear-gradient(135deg,#d2d2d2,#9a9a9a 60%,#6f6f6f)}
  .about{position:absolute;left:186px;top:90px;width:258px}
  .section-title{font-weight:400;font-size:21px;letter-spacing:.3px;margin-bottom:5px;line-height:1.1}
  .body-copy{font-size:13px;line-height:15.8px;font-weight:400}

  .summary{position:absolute;left:32px;top:388px;width:409px;height:186px;border:2px solid var(--ink-light);
           text-align:center;padding:12px 16px 0}
  .summary .section-title{margin-bottom:3px}
  .summary .body-copy{font-size:12.6px;line-height:15.2px}

  .brand-band{position:absolute;left:33px;top:626px;width:277px;height:80px;
              background:linear-gradient(90deg,#3a4b5b,#2c3b49);display:flex;align-items:center;padding-left:28px}
  .code-box{position:absolute;left:310px;top:620px;width:130px;height:92px;background:#fff}

  .brand-name{font-weight:700;color:var(--brand-blue);text-transform:uppercase;letter-spacing:1px;display:flex;align-items:center}
  .brand-mark{display:inline-block;background:var(--brand-blue)}
  .brand-band .brand-name{font-size:20px;line-height:1}
  .brand-band .brand-mark{width:12px;height:12px;margin-right:10px}

  .front-brand{position:absolute;left:40px;top:52px;width:400px;height:86px;display:flex;align-items:center;justify-content:center}
  .front-brand .brand-name{font-size:34px}
  .front-brand .brand-mark{width:22px;height:22px;margin-right:16px}

  .rule{position:absolute;left:0;width:474px;height:7px;background:var(--rule)}
  .rule.top{top:180px}
  .rule.bottom{top:610px}
  .hero{position:absolute;left:0;top:187px;width:474px;height:423px;
        background:linear-gradient(90deg,#2e3c4a 0%,#3a4a59 28%,#9aa2a8 42%,#b4b8bb 50%,#8f979d 58%,#384857 72%,#2c3a47 100%)}

  .front-titles{position:absolute;left:0;top:632px;width:474px;text-align:center}
  .front-titles .kicker{font-weight:600;font-size:13.5px;letter-spacing:.2px;line-height:17.5px}
  .front-titles .subtitle{font-weight:600;font-size:13.5px;line-height:17.5px}
  .front-titles .byline{font-weight:600;font-size:25px;margin-top:14px}

  .spine-brand{position:absolute;left:0;top:234px;width:64px;height:190px}
  .spine-brand .brand-name{position:absolute;left:50%;top:50%;transform:translate(-50%,-50%) rotate(90deg);
        white-space:nowrap;font-size:17px}
  .spine-brand .brand-mark{width:10px;height:10px;margin-right:8px}
  .spine-author{position:absolute;left:0;top:534px;width:64px;height:196px}
  .spine-author span{position:absolute;left:50%;top:50%;transform:translate(-50%,-50%) rotate(90deg);
        white-space:nowrap;color:var(--spine-ink);font-weight:700;font-size:17px}
</style>
</head>
<body>
  <div class="cover">
    <section class="back">
      <svg class="waves" viewBox="0 0 474 756" aria-hidden="true">
        <path d="M0 360 C80 330 160 390 240 360 S400 330 474 355" stroke-width="1.5" stroke-opacity=".16"/>
        <path d="M0 372 C80 342 160 402 240 372 S400 342 474 367" stroke-width="1" stroke-opacity=".1"/>
        <path d="M0 598 C90 570 170 626 250 598 S410 570 474 592" stroke-width="1.5" stroke-opacity=".16"/>
        <path d="M0 610 C90 582 170 638 250 610 S410 582 474 604" stroke-width="1" stroke-opacity=".1"/>
        <path d="M0 735 C90 710 180 755 270 730 S420 712 474 728" stroke-width="1.5" stroke-opacity=".12"/>
      </svg>
      <div class="author-photo" role="img" aria-label="Black and white portrait of the author"></div>
      <div class="about">
        <h2 class="section-title">ABOUT THE AUTHOR:</h2>
        <p class="body-copy">Gregory Talbrecht is a Registered Dietitian and Certified Personal Trainer from Cleveland, OH. He graduated from the Verdant Plains University and currently works as a health coach in the healthcare industry. His passions are fitness, nutrition, science, and motivation. He has extensive knowledge and experience in wellness, healthcare, and disease treatment and disease. Gregory has worked with hundreds of people through counseling, consulting, and coaching in an effort to make a difference in their long-term health. In his spare time, he enjoys exercising, watching movies, and trying out new foods.</p>
      </div>
      <div class="summary">
        <h2 class="section-title">BOOK SUMMARY:</h2>
        <p class="body-copy">Believe in you. Trust in You. Sip. Stroll. Flourish. is a book committed to you. Behavior change and improved health can be challenging. You must feel empowered to make decisions and changes create momentum in the right direction. But, you may not always have the knowledge to do that. This book provides you with practical and fun tools and tips to improve your nutrition, motivation to move, and mindset. You are awesome. You are beautiful. You have the power to control your destiny and future. All you have to do is Sip, Stroll, and Flourish!</p>
      </div>
      <div class="brand-band"><span class="brand-name"><i class="brand-mark"></i>Sip Stroll Flourish</span></div>
      <div class="code-box"></div>
    </section>

    <section class="spine">
      <div class="spine-brand"><span class="brand-name"><i class="brand-mark"></i>Sip Stroll Flourish</span></div>
      <div class="spine-author"><span>Gregory Talbrecht RD, CPT</span></div>
    </section>

    <section class="front">
      <svg class="waves" viewBox="0 0 474 180" aria-hidden="true">
        <path d="M0 150 C80 125 160 175 240 150 S400 125 474 146" stroke-width="1.5" stroke-opacity=".16"/>
        <path d="M0 162 C80 137 160 187 240 162 S400 137 474 158" stroke-width="1" stroke-opacity=".1"/>
      </svg>
      <div class="front-brand"><span class="brand-name"><i class="brand-mark"></i>Sip Stroll Flourish</span></div>
      <div class="rule top"></div>
      <div class="hero" role="img" aria-label="Mountain landscape with a person on a summit raising both arms in a bright vertical light beam"></div>
      <div class="rule bottom"></div>
      <div class="front-titles">
        <p class="kicker">SIP. STROLL. FLOURISH.:</p>
        <p class="subtitle">A Simple Diet, Drive to Stretch, and Outlook Manual Building Traction<br>Along Better Vigor and Balance</p>
        <p class="byline">Gregory Talbrecht RD, CPT</p>
      </div>
    </section>
  </div>
  <div class="floor"></div>
</body>
</html>
```